Physical Therapy Center for children Business Card

We need a Business Card for our company (Physical Therapy for children and youth with special needs) in Lisbon, Portugal. The name of the company is "Luz do Caminho"

The card must contain the following info:
- Logo: see uploaded file
- Name: Luz do Caminho
- Slogan: Plantamos esperança, cuidamos com carinho, celebramos conquistas!
- Service: Terapias Especializadas
- Address: Rua Henrique Valente Morais 4B
- ZipCode: 2719-583 Vale das Amoras
- E-mail: geral@luzina.pt
- Site: www.luzina.pt
- Facebook: www.facebook.com/luzdocaminho
- Phone: +351 21 547 60 29
- Cell Phone: +351 96 718 45 93

The stationary should have contain all info from business card.

Target Market(s)

Parents of children with special needs

Industry/Entity Type

Physical Therapy

Contact Information for Business Card

The card design should be compatible with http://www.vellotype.com/product2/order_detail.php?gid=40

Requirements
Should not have
• The business card should not have a Black background. Use white or other color.

```html
<!DOCTYPE html>
<html lang="pt">
<head>
<meta charset="utf-8">
<title>Luz do Caminho — Cartão de Visita</title>
<link href="https://fonts.googleapis.com/css2?family=PT+Sans:wght@400;700&family=PT+Sans+Narrow:wght@700&display=swap" rel="stylesheet">
<style>
  :root {
    --page-bg: #d9d6d1;
    --card-bg: #eef0ee;
    --band-top: #7d7f80;
    --band-bottom: #9c9e9f;
    --band-text: #f4f4f2;
    --ink: #3a3b3d;
    --ink-soft: #2f3032;
    --teal: #1f9a7f;
    --sun: #f1c232;
    --card-edge: #ffffff;
  }
  * { box-sizing: border-box; margin: 0; padding: 0; }
  html, body { width: 1200px; height: 969px; overflow: hidden; }
  body {
    background: var(--page-bg);
    font-family: "PT Sans", Arial, sans-serif;
    color: var(--ink);
    position: relative;
  }
  .card {
    position: absolute;
    left: 100px;
    top: 198px;
    width: 1000px;
    height: 572px;
    background: var(--card-bg);
    border: 2px solid var(--card-edge);
    border-radius: 34px;
    overflow: hidden;
    box-shadow: 0 10px 30px rgba(0,0,0,0.12);
  }
  .brand-band {
    position: absolute;
    left: 0; top: 0;
    width: 185px; height: 100%;
    background: linear-gradient(180deg, var(--band-top), var(--band-bottom));
  }
  .brand-band__text {
    position: absolute;
    left: 50%; top: 50%;
    width: 560px;
    transform: translate(-50%, -50%) rotate(-90deg);
    text-align: left;
    padding-left: 18px;
  }
  .brand-band__name {
    font-weight: 700;
    font-size: 56px;
    line-height: 1;
    color: var(--band-text);
    letter-spacing: 0.5px;
    white-space: nowrap;
  }
  .brand-band__slogan {
    margin-top: 10px;
    font-size: 17px;
    color: var(--band-text);
    white-space: nowrap;
  }
  .logo-mark {
    position: absolute;
    left: 235px;
    top: 235px;
    display: flex;
    align-items: center;
    gap: 18px;
  }
  .logo-mark__dot {
    width: 46px; height: 46px;
    border-radius: 50%;
    background: var(--sun);
    flex: none;
  }
  .logo-mark__name {
    font-weight: 700;
    font-size: 44px;
    color: var(--teal);
    white-space: nowrap;
  }
  .details {
    position: absolute;
    right: 44px;
    top: 56px;
    text-align: right;
  }
  .details__name {
    font-family: "PT Sans Narrow", "Arial Narrow", sans-serif;
    font-weight: 700;
    font-size: 40px;
    line-height: 1.1;
    color: var(--ink);
    letter-spacing: 0.5px;
  }
  .details__role {
    font-size: 26px;
    color: var(--teal);
    line-height: 1.3;
  }
  .address {
    margin-top: 42px;
    font-style: normal;
    font-size: 26px;
    line-height: 38px;
    color: var(--ink-soft);
  }
  .contacts {
    list-style: none;
    margin-top: 36px;
    font-size: 25px;
    line-height: 38px;
    color: var(--ink-soft);
  }
  .contacts li {
    display: flex;
    justify-content: flex-end;
    align-items: center;
    gap: 12px;
  }
  .contacts svg { width: 22px; height: 22px; flex: none; fill: var(--ink); }
</style>
</head>
<body>
  <main class="card">
    <aside class="brand-band">
      <div class="brand-band__text">
        <div class="brand-band__name">Luz do Caminho</div>
        <div class="brand-band__slogan">Plantamos esperança, cuidamos com carinho, celebramos conquistas</div>
      </div>
    </aside>

    <div class="logo-mark">
      <span class="logo-mark__dot"></span>
      <span class="logo-mark__name">Luz do Caminho</span>
    </div>

    <section class="details">
      <div class="details__name">RUI MARQUES</div>
      <div class="details__role">CEO/Founder</div>
      <address class="address">
        Rua Henrique Valente<br>
        Morais 4B<br>
        ZipCode: 2719-583 Vale<br>
        das Amoras
      </address>
      <ul class="contacts">
        <li>+351 21 547 60 29
          <svg viewBox="0 0 24 24" aria-hidden="true"><path d="M6.6 10.8a15.1 15.1 0 0 0 6.6 6.6l2.2-2.2c.3-.3.7-.4 1-.2 1.1.4 2.3.6 3.6.6.6 0 1 .4 1 1V20c0 .6-.4 1-1 1A17 17 0 0 1 3 4c0-.6.4-1 1-1h3.5c.6 0 1 .4 1 1 0 1.3.2 2.5.6 3.6.1.3 0 .7-.2 1z"/></svg>
        </li>
        <li>+351 96 718 45 93
          <svg viewBox="0 0 24 24" aria-hidden="true"><path d="M7 1h10a2 2 0 0 1 2 2v18a2 2 0 0 1-2 2H7a2 2 0 0 1-2-2V3a2 2 0 0 1 2-2zm0 3v15h10V4zm5 16.2a.9.9 0 1 0 0 1.8.9.9 0 0 0 0-1.8z"/></svg>
        </li>
        <li>geral@luzina.pt
          <svg viewBox="0 0 24 24" aria-hidden="true"><path d="M2 5h20v14H2zm2 2v.4l8 5.2 8-5.2V7zm0 2.8V17h16V9.8l-8 5.2z"/></svg>
        </li>
        <li>www.luzina.pt
          <svg viewBox="0 0 24 24" aria-hidden="true"><path d="M12 2a10 10 0 1 0 0 20 10 10 0 0 0 0-20zm0 2a8 8 0 0 1 0 16 8 8 0 0 1 0-16zm-1 3c-2 1-3 3-2 4l2 1v3l2 2 1-3 2-1-1-3h-3z"/></svg>
        </li>
        <li>luzdocaminho
          <svg viewBox="0 0 24 24" aria-hidden="true"><rect x="3" y="3" width="18" height="18" rx="2"/></svg>
        </li>
      </ul>
    </section>
  </main>
</body>
</html>
```